Online Home Automation business needs business card design

New business starting up that sells home-automation products in Australia. Business card needs to look very polished and professional. The business name is "Vesk Automation".
Updates

Thank you all for the great designs, We are really impressed. We are in the process of deciding on a design but keep the designs coming in.

Industry/Entity Type

Business

```html
<!DOCTYPE html>
<html lang="en">
<head>
<meta charset="utf-8">
<title>Vesk Automation – Business Card</title>
<link rel="stylesheet" href="https://fonts.googleapis.com/css2?family=Quicksand:wght@400;500&family=Ubuntu:wght@400&display=swap">
<style>
  :root {
    --card-black: #0b0b0b;
    --card-charcoal: #1e1e1e;
    --brand-red: #e3070d;
    --brand-red-deep: #b80408;
    --band-ink: #151515;
    --brand-white: #f4f4f4;
  }
  html, body {
    margin: 0;
    padding: 0;
    overflow: hidden;
    background: var(--card-black);
  }
  .card {
    position: relative;
    width: 1200px;
    height: 702px;
    overflow: hidden;
    background:
      radial-gradient(ellipse at 30% 40%, var(--card-charcoal) 0%, rgba(20,20,20,0.6) 35%, transparent 70%),
      radial-gradient(ellipse at 80% 85%, #161616 0%, transparent 55%),
      var(--card-black);
  }
  .brand-mark {
    position: absolute;
    left: 62px;
    top: 32px;
    width: 240px;
    height: 240px;
    border-radius: 50%;
    background: var(--brand-red);
  }
  .brand-name {
    position: absolute;
    left: 50px;
    top: 292px;
    margin: 0;
    font-family: "Ubuntu", sans-serif;
    font-weight: 400;
    color: var(--brand-white);
    line-height: 1.18;
  }
  .brand-name__first {
    display: block;
    font-size: 100px;
  }
  .brand-name__second {
    display: block;
    font-size: 84px;
  }
  .contact-band {
    position: absolute;
    right: 0;
    height: 88px;
    display: flex;
    align-items: center;
    justify-content: flex-end;
    padding-right: 18px;
    box-sizing: border-box;
    background:
      radial-gradient(ellipse at 25% 40%, rgba(255,60,60,0.35) 0%, transparent 55%),
      radial-gradient(ellipse at 75% 70%, rgba(120,0,0,0.35) 0%, transparent 60%),
      linear-gradient(90deg, var(--brand-red-deep), var(--brand-red) 40%, var(--brand-red));
    font-family: "Quicksand", sans-serif;
    font-weight: 500;
    color: var(--band-ink);
    white-space: nowrap;
  }
  .contact-band--name  { left: 509px; top: 155px; font-size: 50px; letter-spacing: 1px; }
  .contact-band--web   { left: 581px; top: 279px; font-size: 31px; letter-spacing: -0.5px; }
  .contact-band--email { left: 645px; top: 396px; font-size: 29px; letter-spacing: -0.5px; }
  .contact-band--phone { left: 735px; top: 520px; font-size: 37px; }
</style>
</head>
<body>
  <main class="card">
    <div class="brand-mark" aria-hidden="true"></div>
    <h1 class="brand-name">
      <span class="brand-name__first">Vesk</span>
      <span class="brand-name__second">Automation</span>
    </h1>
    <div class="contact-band contact-band--name">Marek Lund</div>
    <div class="contact-band contact-band--web">www.veskautomation.com.au</div>
    <div class="contact-band contact-band--email">info@veskautomation.com.au</div>
    <div class="contact-band contact-band--phone">+61 400 555 219</div>
  </main>
</body>
</html>
```